VORTAL Business Card Design

We need a business card for a new company based on the Gold Coast, we are a new supplement distributing company called VORTAL Sports Nutrition - Bold Horizon Sports Nutrition. We are providing new science based bodybuilding and fitness supplementation. Our company has a key focus towards next generation. We are wanting a card that is cool, innovative and fresh. We would like to see the implementation of the below image in a fresh and very innovative design that stands out. The final design should communicate New, Innovative, Cool, Science and researched based.
Target Market(s)
The target market is fitness and bodybuilder enthusiasts. Young audience so very cool looking.
Industry/Entity Type
Fitness
Contact Information for Business Card
(front of card)
VORTAL Sports Nutrition.
Liam Darrow
CEO/Sport Nutrition Specialist
0472 638 904
Liam@vortalsportsfuel.example
www.vortalsportsfuel.example
(back of card)
Scientifically formulated supplement range
Private Nutrition consultations
comprehensive sports nutrition seminars
Requirements
Nice to have
- The card could have a cut out on one of the sides or one of the corners rounded off so the card looks different from a normal business card.
Should not have
- The colours need to complement each other and pop out.

```html
<!DOCTYPE html>
<html lang="en">
<head>
<meta charset="UTF-8">
<title>VORTAL Sports Nutrition – Business Card</title>
<link href="https://fonts.googleapis.com/css2?family=Orbitron:wght@500;700;800&family=Michroma&family=Exo+2:wght@300;400&display=swap" rel="stylesheet">
<style>
  :root {
    --page-bg: #ffffff;
    --card-bg: #000000;
    --cyan: #2ee6e6;
    --cyan-soft: #7ff3f3;
    --glow: rgba(70, 225, 235, 0.55);
    --white: #f2f2f2;
    --rule: #1c5f66;
  }
  * { margin: 0; padding: 0; box-sizing: border-box; }
  html, body {
    width: 1200px; height: 410px; overflow: hidden;
    background: var(--page-bg);
  }
  .canvas { position: relative; width: 1200px; height: 410px; }
  .canvas::after {
    content: ""; position: absolute; left: 0; right: 0; top: 407px;
    height: 1px; background: #e4e4e4;
  }
  .card {
    position: absolute; top: 28px; width: 567px; height: 349px;
    background: var(--card-bg);
    box-shadow: 0 0 10px 3px var(--glow);
    text-align: center;
  }
  .card--front { left: 16px; border-radius: 30px 4px 30px 4px; }
  .card--back  { left: 615px; border-radius: 4px 30px 4px 30px; }

  .brand-mark {
    position: absolute; left: 50%; top: 29px; transform: translateX(-50%);
    width: 122px; height: 122px; border-radius: 50%;
    border: 2px solid var(--cyan-soft);
    box-shadow: 0 0 6px var(--glow);
    display: flex; align-items: center; justify-content: center;
  }
  .brand-name {
    font-family: "Orbitron", sans-serif; font-weight: 800;
    font-size: 19px; letter-spacing: 1px; color: var(--cyan);
  }
  .tagline {
    position: absolute; left: 0; right: 0; top: 162px;
    font-family: "Orbitron", sans-serif; font-weight: 700;
    font-size: 17px; letter-spacing: 0.6px; color: var(--cyan);
  }
  .contact { position: absolute; left: 0; right: 0; top: 201px; }
  .contact__name {
    font-family: "Michroma", sans-serif; font-size: 15px;
    color: var(--white); letter-spacing: 0.5px; line-height: 20px;
  }
  .contact__role {
    font-family: "Exo 2", sans-serif; font-weight: 300;
    font-size: 11.5px; color: var(--cyan); line-height: 18px;
  }
  .contact__phone {
    font-family: "Orbitron", sans-serif; font-weight: 700;
    font-size: 15px; color: var(--white); letter-spacing: 0.6px;
    line-height: 24px; margin-top: 2px;
  }
  .contact__email {
    font-family: "Exo 2", sans-serif; font-weight: 400;
    font-size: 14px; color: var(--white); line-height: 22px;
  }
  .rule {
    position: absolute; height: 1px;
    background: linear-gradient(90deg, transparent, var(--rule) 15%, var(--cyan) 50%, var(--rule) 85%, transparent);
  }
  .card--front .rule { left: 48px; right: 48px; top: 302px; }
  .website {
    position: absolute; left: 0; right: 0; top: 316px;
    font-family: "Orbitron", sans-serif; font-weight: 700;
    font-size: 13.5px; color: var(--cyan); letter-spacing: 0.4px;
  }
  .card--back .rule--top { left: 50px; right: 60px; top: 218px; }
  .card--back .rule--bottom { left: 50px; right: 60px; top: 298px; }
  .services {
    position: absolute; left: 72px; top: 228px; list-style: none; text-align: left;
  }
  .services li {
    position: relative; padding-left: 33px;
    font-family: "Michroma", sans-serif; font-size: 13px;
    color: var(--cyan); line-height: 20px; letter-spacing: 0.2px;
  }
  .services li::before {
    content: ""; position: absolute; left: 0; top: 6px;
    width: 8px; height: 8px; border-radius: 50%; background: var(--cyan);
  }
</style>
</head>
<body>
<main class="canvas">
  <section class="card card--front" aria-label="Business card front">
    <div class="brand-mark"><span class="brand-name">VORTAL</span></div>
    <h1 class="tagline">BOLD HORIZON SPORTS NUTRITION</h1>
    <div class="contact">
      <p class="contact__name">LIAM DARROW</p>
      <p class="contact__role">CEO/Sport Nutrition Specialist</p>
      <p class="contact__phone">0472 638 904</p>
      <p class="contact__email">liam@vortalsportsfuel.example</p>
    </div>
    <div class="rule"></div>
    <p class="website">www.vortalsportsfuel.example</p>
  </section>

  <section class="card card--back" aria-label="Business card back">
    <div class="brand-mark"><span class="brand-name">VORTAL</span></div>
    <h2 class="tagline">BOLD HORIZON SPORTS NUTRITION</h2>
    <div class="rule rule--top"></div>
    <ul class="services">
      <li>Scientifically formulated supplement range</li>
      <li>Private nutrition consultations</li>
      <li>Comprehensive sports nutrition seminars</li>
    </ul>
    <div class="rule rule--bottom"></div>
  </section>
</main>
</body>
</html>
```